Starting number decals Motorsport
Frost Rally Days 2013
Now it is only 1 day and 14 hours left!!!
torvald
We have some excellent suggestions and to see how the sticker will look on a car in the real world,
we have loaded a picture now We send a test picture that it is possible to test mount the decal on the side of the car, we want to mount on the front door of the car, the picture is uploaded now
We want to try to tilt the stratnumer figures a little forward as PRIMTOUR
We have now updated with sponsor logo will be featured on the decal
KR/WTF/HV Team.
Forgot to inform that 5 year anniversary is this year and it should be, if possible, preferably also in 2013

```html
<!DOCTYPE html>
<html lang="sv">
<head>
<meta charset="utf-8">
<title>Frost Rally Days 2013 – startnummer</title>
<link href="https://fonts.googleapis.com/css2?family=Exo+2:ital,wght@0,700;0,900;1,900&family=Roboto:wght@500;700;900&display=swap" rel="stylesheet">
<style>
  :root{
    --page:#e8ebef;
    --white:#ffffff;
    --ink:#1d1d1f;
    --red:#e3262c;
    --navy:#1a2f86;
    --blue-deep:#1b3aa0;
    --blue-mid:#2b6fd0;
    --blue-light:#3f93e8;
    --yellow:#ffd21a;
    --flag-blue:#1e5fb4;
    --strip:#f3f5f8;
    --grey:#6c7480;
  }
  *{box-sizing:border-box;margin:0;padding:0}
  html,body{width:1200px;height:799px;overflow:hidden;background:var(--page)}
  .canvas{position:relative;width:1200px;height:799px}
  .decal{
    position:absolute;left:240px;top:42px;width:720px;height:714px;
    background:var(--white);border:3px solid #c9ced6;
    display:flex;flex-direction:column;overflow:hidden;
    font-family:"Roboto",sans-serif;
  }
  .decal-header{height:130px;padding:14px 24px 8px;display:flex;flex-direction:column;justify-content:space-between}
  .sponsor-row{display:flex;align-items:center;justify-content:space-between}
  .event-name{font-family:"Exo 2",sans-serif;font-weight:900;font-size:40px;color:var(--red);letter-spacing:-.5px}
  .partner{display:flex;align-items:center;gap:10px}
  .partner-dot{width:40px;height:40px;border-radius:50%;background:var(--flag-blue)}
  .partner-name{font-weight:700;font-size:22px;color:var(--navy);line-height:1.05;width:170px}
  .event-caption{font-weight:700;font-size:17px;color:var(--ink);letter-spacing:.3px}
  .number-panel{
    height:400px;
    background:radial-gradient(ellipse at 50% 45%,var(--blue-light) 0%,var(--blue-mid) 45%,var(--blue-deep) 100%);
    display:flex;flex-direction:column;align-items:center;justify-content:center;gap:4px;
  }
  .start-number{
    font-family:"Exo 2",sans-serif;font-weight:900;font-style:italic;
    font-size:210px;line-height:.95;color:var(--red);
    -webkit-text-stroke:6px var(--yellow);paint-order:stroke fill;letter-spacing:4px;
    transform:skewX(-6deg);
  }
  .class-code{
    font-family:"Exo 2",sans-serif;font-weight:900;font-style:italic;
    font-size:112px;line-height:1;color:var(--yellow);letter-spacing:6px;
    transform:skewX(-6deg);
  }
  .inspection-strip{
    height:92px;background:linear-gradient(var(--white),var(--strip));
    display:grid;grid-template-columns:1fr 150px 1fr;align-items:center;padding:0 26px;
    font-weight:900;font-size:26px;color:var(--ink);letter-spacing:1px
  }
  .inspection-strip .speed{text-align:right}
  .flag{width:150px;height:92px;display:block}
  .decal-footer{flex:1;display:flex;align-items:center;justify-content:center;gap:12px}
  .footer-square{width:22px;height:22px;background:var(--red)}
  .footer-name{font-weight:900;font-size:38px;color:var(--navy);letter-spacing:2px}
</style>
</head>
<body>
<main class="canvas">
  <section class="decal" aria-label="Startnummerdekal Frost Rally Days 2013">
    <header class="decal-header">
      <div class="sponsor-row">
        <span class="event-name">Frost Rally Days</span>
        <div class="partner">
          <span class="partner-dot"></span>
          <span class="partner-name">Nordvik Fordon AB</span>
        </div>
      </div>
      <p class="event-caption">5th Anniversary FRD 13-14.7 2013</p>
    </header>
    <div class="number-panel">
      <div class="start-number">1234</div>
      <div class="class-code">16 BD</div>
    </div>
    <div class="inspection-strip">
      <span class="inspection">BESIKTNING</span>
      <svg class="flag" viewBox="0 0 150 92" aria-hidden="true">
        <rect width="150" height="92" fill="var(--flag-blue)"/>
        <rect x="44" y="0" width="20" height="92" fill="var(--yellow)"/>
        <rect x="0" y="36" width="150" height="20" fill="var(--yellow)"/>
      </svg>
      <span class="speed">FART / 110</span>
    </div>
    <footer class="decal-footer">
      <span class="footer-square"></span>
      <span class="footer-name">BANKLUBBEN</span>
    </footer>
  </section>
</main>
</body>
</html>
```